Trevolina corporate powerpoint

Hi,
I am creating my own web3 and blockchain academy.

I would like to obtain pricing for a complete corporate powerpoint template for my training sessions in companies and bussiness schools

. I am sharing with you my logo in order to show you my colours.
If you can improve my logo, it will be perfect too. (full pack to launch it)

Thanks
Updates

designers are asiking for an extension

Target Market(s)

Companies and Business Schools

Industry/Entity Type

academy

Font styles to use
Sans Serif
Other font styles liked:
• Arial, Calibri

Colors
0054AA
0677BA
7BADD7
CADEEF
E8F1F8
0094D4
00A9DD
6FCCEA
C7EBF8
E9F6FB
00AB8E
00BBA5
67D7C9
C6EFE9
E9F9F6
F0912C
F2A743
F7CA91
FBE8D2
FDF5EE
EE7325
F08F49
F5BC92
FAE3D3
FDF4ED
6B429C
8869AF
B7A5CE
E3DAEB
F3F0F8

Requirements
Must have
• Blockchain thematic, withe and dark (not black) slides

```html
<!DOCTYPE html>
<html lang="en">
<head>
<meta charset="utf-8">
<title>Trevolina corporate presentation</title>
<link href="https://fonts.googleapis.com/css2?family=Poppins:wght@400;600;700;800&family=Open+Sans:wght@300;400;700&display=swap" rel="stylesheet">
<style>
:root{
  --bg:#d6d6d6;
  --white:#ffffff;
  --dark:#2e2e2e;
  --ink:#1a1a1a;
  --cyan:#2ee6dc;
  --sky:#2bbaf5;
  --lilac:#c6b2f3;
  --teal-text:#38c9d9;
  --muted:#555;
  --grad:linear-gradient(90deg,var(--lilac) 0%,var(--sky) 35%,var(--cyan) 100%);
  --grad-v:linear-gradient(180deg,var(--cyan) 0%,var(--sky) 70%,var(--lilac) 100%);
}
*{margin:0;padding:0;box-sizing:border-box}
html,body{width:898px;height:1200px;overflow:hidden;background:var(--bg)}
body{position:relative;font-family:"Open Sans",Arial,sans-serif;color:var(--ink)}
.slide{position:absolute;background:var(--white);overflow:hidden;box-shadow:0 2px 5px rgba(0,0,0,.25)}
.slide.small{width:247px;height:139px}
.slide.dark{background:var(--dark);color:#fff}
.abs{position:absolute}
.photo{position:absolute}
.grad{background:var(--grad)}
.grad-v{background:var(--grad-v)}
.page-no{position:absolute;right:8px;bottom:7px;width:15px;height:7px;background:var(--sky);color:var(--ink);font:600 5px/7px Poppins,sans-serif;text-align:center}
.page-no.inv{background:var(--ink);color:#fff}
.mini-brand{position:absolute;left:7px;bottom:6px;width:11px;height:9px;border:0.6px solid var(--sky);font:700 2px/8px Poppins,sans-serif;text-align:center;color:var(--ink);background:#fff}
.tiny{font-size:2.6px;line-height:3.5px;color:var(--muted)}
.tiny b{color:var(--ink)}
.dark .tiny{color:#ddd}
.cyan-title{font-family:Poppins,sans-serif;font-weight:600;color:var(--teal-text);letter-spacing:.5px}

/* hero */
.hero{left:60px;top:63px;width:772px;height:434px}
.hero-dark{left:332px;top:0;width:440px;height:434px;background:var(--dark)}
.hero-globe{left:332px;top:0;width:440px;height:434px;background:radial-gradient(circle at 66% 52%,#cfcfcf 0%,#8a8a8a 18%,#4a4a4a 34%,rgba(46,46,46,0) 55%)}
.brand-box{left:42px;top:22px;width:87px;height:87px;border:3px solid var(--sky);border-left-color:var(--lilac);border-top-color:var(--cyan);background:#fff;display:flex;align-items:center;justify-content:center}
.brand-box span{font:700 14px Poppins,sans-serif;color:var(--ink)}
.headline-band{left:30px;top:163px;width:419px;height:107px}
.headline{left:45px;top:168px;font:800 42px/46px Poppins,sans-serif;color:#fff;letter-spacing:-.5px}
.headline .line2{color:var(--ink)}
.hero-rule{left:36px;top:392px;width:132px;height:1px;background:var(--ink)}
.hero-tag{left:177px;top:387px;font:400 7.5px Poppins,sans-serif;letter-spacing:1px}
.social{position:absolute;top:33px;width:30px;height:30px;border-radius:50%;background:var(--grad)}

/* shared pieces */
.icon-tile{position:absolute;width:27px;height:27px;background:var(--grad-v);display:flex;align-items:center;justify-content:center}
.gauge{position:absolute;width:34px;height:34px}
</style>
</head>
<body>

<!-- Title slide -->
<section class="slide hero">
  <div class="abs hero-dark"></div>
  <div class="abs hero-globe" role="img" aria-label="Glowing digital globe wrapped in a network of connected nodes"></div>
  <div class="abs brand-box"><span>Trevolina</span></div>
  <div class="abs headline-band grad"></div>
  <h1 class="abs headline">HEADLINE<br><span class="line2">PRESENTATION.</span></h1>
  <div class="abs hero-rule"></div>
  <p class="abs hero-tag">LOREM IPSUM DOLOR SIT</p>
  <span class="social" style="left:635px"></span>
  <span class="social" style="left:678px"></span>
  <span class="social" style="left:721px"></span>
</section>

<!-- 02 Contents -->
<section class="slide small" style="left:60px;top:521px">
  <div class="abs grad-v" style="left:0;top:0;width:85px;height:80px"></div>
  <div class="photo" role="img" aria-label="Hand holding a tablet projecting a holographic globe" style="left:41px;top:16px;width:85px;height:105px;background:linear-gradient(160deg,#777,#2b2b2b)"></div>
  <h2 class="abs cyan-title" style="left:133px;top:22px;font-size:12px">Contents</h2>
  <div class="abs tiny" style="left:133px;top:41px;width:65px"><b>Lorem ipsum</b><br>Lorem ipsum dolor sit amet, consectetuer adipiscing elit, sed diam nonummy nibh</div>
  <div class="abs tiny" style="left:133px;top:62px;width:65px"><b>Lorem ipsum</b><br>Lorem ipsum dolor sit amet, consectetuer adipiscing elit, sed diam nonummy nibh</div>
  <div class="abs tiny" style="left:133px;top:83px;width:65px"><b>Lorem ipsum</b><br>Lorem ipsum dolor sit amet, consectetuer adipiscing elit, sed diam nonummy nibh</div>
  <div class="abs tiny" style="left:133px;top:104px;width:65px"><b>Lorem ipsum</b><br>Lorem ipsum dolor sit amet, consectetuer adipiscing elit, sed diam nonummy nibh</div>
  <div class="mini-brand">Trevolina</div>
  <div class="page-no">02</div>
</section>

<!-- 03 -->
<section class="slide small" style="left:322px;top:521px">
  <h2 class="abs cyan-title" style="left:18px;top:10px;font-size:10px;line-height:13px">Lorem<br>Ipsum sit</h2>
  <p class="abs" style="right:14px;top:14px;font:italic 3px Open Sans,sans-serif;color:#777">DOLOR SIT AMET</p>
  <p class="abs tiny" style="left:18px;top:50px;width:68px">Lorem ipsum dolor sit amet, consectetuer adipiscing elit, sed diam nonummy nibh euismod tincidunt ut laoreet dolore magna aliquam erat volutpat. Ut wisi enim ad minim veniam, quis nostrud exerci tation ullamcorper suscipit lobortis.</p>
  <p class="abs tiny" style="left:24px;top:94px;width:62px"><b>Lorem ipsum dolor sit amet, consectetuer adipiscing elit</b></p>
  <p class="abs tiny" style="left:24px;top:105px;width:62px"><b>Lorem ipsum dolor sit amet, consectetuer adipiscing elit</b></p>
  <div class="abs grad" style="left:108px;top:28px;width:114px;height:72px"></div>
  <div class="photo" role="img" aria-label="Team at a desk reviewing printed charts and laptops" style="left:118px;top:37px;width:113px;height:79px;background:linear-gradient(135deg,#8a8a8a,#3a3a3a)"></div>
  <div class="mini-brand">Trevolina</div>
  <div class="page-no">03</div>
</section>

<!-- 04 About us -->
<section class="slide small" style="left:584px;top:521px">
  <p class="abs" style="left:6px;top:108px;transform:rotate(-90deg);transform-origin:left top;font:300 12px Open Sans,sans-serif;letter-spacing:2px;white-space:nowrap">ABOUT US</p>
  <div class="photo" role="img" aria-label="Blue and teal digital globe made of connected points" style="left:50px;top:0;width:108px;height:139px;background:linear-gradient(90deg,#0e5a55 0%,#1a9fb0 45%,#2b6fd0 75%,#7d6ad0 100%)"></div>
  <h2 class="abs cyan-title" style="left:173px;top:40px;font-size:10px;line-height:11px">Lorem<br>ipsum</h2>
  <p class="abs tiny" style="left:173px;top:67px;width:62px">Lorem ipsum dolor sit amet, consectetuer adipiscing elit, sed diam nonummy nibh euismod tincidunt ut laoreet dolore magna aliquam erat volutpat. Ut wisi enim ad minim veniam.</p>
  <p class="abs tiny" style="left:173px;top:95px;width:62px"><b>Duis autem vel eum iriure dolor in hendrerit in vulputate velit esse.</b></p>
  <div class="mini-brand">Trevolina</div>
  <div class="page-no">04</div>
</section>

<!-- 05 What we do -->
<section class="slide small dark" style="left:60px;top:680px">
  <h2 class="abs" style="left:0;width:247px;top:16px;text-align:center;font:300 13px Open Sans,sans-serif;letter-spacing:2px">WHAT WE DO</h2>
  <p class="abs tiny" style="left:78px;top:35px;width:92px;text-align:center">Lorem ipsum dolor sit amet, consectetuer adipiscing elit, sed diam nonummy. <b style="color:#fff">Ut wisi enim ad minim veniam.</b></p>
  <p class="abs tiny" style="left:30px;top:56px;width:54px;text-align:right">Lorem ipsum dolor sit amet, consectetuer adipiscing elit, sed diam nonummy.</p>
  <p class="abs tiny" style="left:170px;top:56px;width:54px">Lorem ipsum dolor sit amet, consectetuer adipiscing elit, sed diam nonummy.</p>
  <p class="abs tiny" style="left:30px;top:94px;width:54px;text-align:right">Lorem ipsum dolor sit amet, consectetuer adipiscing elit, sed diam nonummy.</p>
  <p class="abs tiny" style="left:170px;top:94px;width:54px">Lorem ipsum dolor sit amet, consectetuer adipiscing elit, sed diam nonummy.</p>
  <div class="icon-tile" style="left:90px;top:51px"><svg width="16" height="16" viewBox="0 0 16 16" fill="none" stroke="#1a1a1a" stroke-width="1"><circle cx="8" cy="8" r="2.5"/><circle cx="8" cy="8" r="5.5" stroke-dasharray="2.2 1.3"/></svg></div>
  <div class="icon-tile" style="left:131px;top:51px"><svg width="16" height="16" viewBox="0 0 16 16" fill="none" stroke="#1a1a1a" stroke-width="1"><rect x="4" y="4" width="8" height="8"/><path d="M6 2v2M8 2v2M10 2v2M6 12v2M8 12v2M10 12v2M2 6h2M2 8h2M2 10h2M12 6h2M12 8h2M12 10h2"/></svg></div>
  <div class="icon-tile" style="left:90px;top:87px"><svg width="16" height="16" viewBox="0 0 16 16" fill="none" stroke="#1a1a1a" stroke-width="1"><rect x="2" y="3" width="12" height="8"/><path d="M6 14h4M8 11v3"/></svg></div>
  <div class="icon-tile" style="left:131px;top:87px"><svg width="16" height="16" viewBox="0 0 16 16" fill="none" stroke="#1a1a1a" stroke-width="1"><path d="M4.5 12h7.5a2.5 2.5 0 0 0 0-5 3.5 3.5 0 0 0-6.8-.8A2.8 2.8 0 0 0 4.5 12z"/></svg></div>
  <div class="mini-brand" style="background:var(--dark);color:#fff">Trevolina</div>
  <div class="page-no">05</div>
</section>

<!-- 06 Bar chart -->
<section class="slide small" style="left:322px;top:680px">
  <h2 class="abs cyan-title" style="left:20px;top:8px;font-size:12px">Bar chart</h2>
  <p class="abs tiny" style="left:20px;top:30px;width:72px">Lorem ipsum dolor sit amet, consectetuer adipiscing elit, sed diam nonummy nibh euismod tincidunt ut laoreet dolore magna</p>
  <p class="abs tiny" style="left:20px;top:49px;width:72px">Lorem ipsum dolor sit amet, consectetuer adipiscing elit, sed diam nonummy nibh euismod tincidunt ut laoreet dolore magna</p>
  <svg class="abs" style="left:14px;top:74px" width="108" height="50" viewBox="0 0 108 50">
    <defs><linearGradient id="areaFill" x1="0" x2="1"><stop offset="0" stop-color="#2ee6dc"/><stop offset="1" stop-color="#c6b2f3"/></linearGradient></defs>
    <g font-family="Open Sans" font-size="2.4" fill="#333"><text x="0" y="3">1000</text><text x="0" y="11">700</text><text x="0" y="19">500</text><text x="0" y="27">300</text><text x="0" y="35">100</text><text x="0" y="43">0</text></g>
    <line x1="8" y1="2" x2="8" y2="45" stroke="#333" stroke-width=".3"/>
    <path d="M14 44 C20 38,24 38,28 41 C33 44,35 32,40 32 C44 32,46 40,50 38 C55 36,58 20,64 20 C70 20,70 36,76 38 L86 42 L86 44 Z" fill="url(#areaFill)"/>
    <g font-family="Open Sans" font-style="italic" font-size="2.6" fill="#333"><text x="20" y="34">100</text><text x="33" y="39">20</text><text x="38" y="28">275</text><text x="52" y="34">130</text><text x="60" y="17">650</text><text x="80" y="36">80</text></g>
  </svg>
  <div class="abs grad-v" style="left:122px;top:0;width:125px;height:139px"></div>
  <p class="abs" style="left:140px;top:26px;font:600 3.6px Poppins,sans-serif">LOREM IPSUM</p>
  <p class="abs" style="left:195px;top:26px;font:600 3.6px Poppins,sans-serif">LOREM IPSUM</p>
  <svg class="gauge" style="left:140px;top:35px" viewBox="0 0 34 34"><circle cx="17" cy="17" r="15" fill="none" stroke="#1a1a1a" stroke-width="1.2" stroke-dasharray="70 30"/><circle cx="17" cy="17" r="15" fill="none" stroke="#fff" stroke-width="1.2" stroke-dasharray="25 75" stroke-dashoffset="-70"/><text x="17" y="18.5" text-anchor="middle" font-family="Poppins" font-weight="600" font-size="5" letter-spacing="1">4356</text><text x="17" y="22" text-anchor="middle" font-size="1.6">LOREM IPSUM</text></svg>
  <svg class="gauge" style="left:195px;top:35px" viewBox="0 0 34 34"><circle cx="17" cy="17" r="15" fill="none" stroke="#1a1a1a" stroke-width="1.2" stroke-dasharray="60 40"/><circle cx="17" cy="17" r="15" fill="none" stroke="#fff" stroke-width="1.2" stroke-dasharray="35 65" stroke-dashoffset="-60"/><text x="17" y="18.5" text-anchor="middle" font-family="Poppins" font-weight="600" font-size="5" letter-spacing="1">2164</text><text x="17" y="22" text-anchor="middle" font-size="1.6">LOREM IPSUM</text></svg>
  <p class="abs tiny" style="left:134px;top:82px;width:100px;color:#1a1a1a">Strategizing the right timing that fits your customers' buying cycles will help you save money and maximize sales. The marketing plan should be innovative.</p>
  <p class="abs tiny" style="left:134px;top:98px;width:100px;color:#1a1a1a">It should have the details on how your sales are followed up and the activities you are doing to develop your offers.</p>
  <div class="mini-brand">Trevolina</div>
  <div class="page-no inv">06</div>
</section>

<!-- 07 Services -->
<section class="slide small" style="left:584px;top:680px">
  <div class="abs" style="left:0;top:0;width:70px;height:139px;background:var(--dark)"></div>
  <h2 class="abs cyan-title" style="left:90px;top:12px;font-size:11px;letter-spacing:1.5px">SERVICES</h2>
  <p class="abs tiny" style="left:168px;top:14px;width:66px;text-align:right">Duis autem vel eum iriure dolor in hendrerit in vulputate velit esse molestie consequat.</p>
  <div class="abs grad" style="left:0;top:35px;width:5px;height:69px"></div>
  <div class="abs" style="left:59px;top:35px;width:188px;height:69px;background:linear-gradient(90deg,var(--cyan),var(--sky) 70%,var(--lilac))"></div>
  <div class="photo" role="img" aria-label="Person touching a glowing digital globe interface" style="left:25px;top:44px;width:34px;height:44px;background:linear-gradient(135deg,#999,#222)"></div>
  <h3 class="abs" style="left:92px;top:46px;font:600 10px/12px Poppins,sans-serif;color:var(--ink);letter-spacing:.5px">Lorem<br>Ipsum sit</h3>
  <p class="abs tiny" style="left:92px;top:75px;width:145px;color:#1a1a1a">Lorem ipsum dolor sit amet, consectetuer adipiscing elit, sed diam nonummy nibh euismod tincidunt ut laoreet dolore magna aliquam erat volutpat. Ut wisi enim ad minim veniam, quis nostrud exerci tation ullamcorper suscipit lobortis nisl ut aliquip.</p>
  <p class="abs tiny" style="left:98px;top:108px;width:60px"><b>Lorem ipsum dolor sit amet, consectetuer adipiscing elit</b></p>
  <p class="abs tiny" style="left:170px;top:108px;width:60px"><b>Lorem ipsum dolor sit amet, consectetuer adipiscing elit</b></p>
  <div class="mini-brand" style="background:var(--dark);color:#fff">Trevolina</div>
  <div class="page-no">07</div>
</section>

<!-- 08 -->
<section class="slide small" style="left:60px;top:838px">
  <div class="abs" style="left:0;top:0;width:247px;height:72px;background:linear-gradient(90deg,var(--cyan),var(--sky) 75%,var(--lilac))"></div>
  <div class="abs" style="left:21px;top:18px;width:66px;height:112px;background:var(--dark)"></div>
  <h2 class="abs cyan-title" style="left:28px;top:21px;font-size:10px;line-height:12px;color:var(--cyan)">Lorem<br>Ipsum sit</h2>
  <p class="abs tiny" style="left:28px;top:48px;width:54px;color:#ddd">Lorem ipsum dolor sit amet, consectetuer adipiscing elit, sed diam nonummy nibh euismod tincidunt ut laoreet dolore magna aliquam erat volutpat. Ut wisi enim ad minim veniam.</p>
  <p class="abs tiny" style="left:28px;top:88px;width:54px;color:#ddd">Lorem ipsum dolor sit amet, consectetuer adipiscing elit, sed diam nonummy nibh euismod tincidunt ut laoreet dolore magna.</p>
  <div class="photo" role="img" aria-label="Handshake overlaid with network icons of people" style="left:106px;top:18px;width:119px;height:98px;background:linear-gradient(135deg,#aaa,#444)"></div>
  <div class="mini-brand">Trevolina</div>
  <div class="page-no">08</div>
</section>

<!-- 09 Product features -->
<section class="slide small" style="left:322px;top:838px">
  <div class="abs" style="left:0;top:0;width:84px;height:139px;background:linear-gradient(180deg,var(--cyan),var(--sky))"></div>
  <h2 class="abs" style="left:13px;top:22px;font:400 7px/9px Open Sans,sans-serif;color:#222">PRODUCT<br>FEATURES AND<br><b>FUNCTIONALITY</b></h2>
  <p class="abs tiny" style="left:13px;top:52px;width:62px;color:#1a1a1a">Lorem ipsum dolor sit amet, consectetuer adipiscing elit, sed diam nonummy nibh euismod tincidunt ut laoreet dolore magna aliquam erat volutpat. Ut wisi enim ad minim veniam, quis nostrud exerci tation.</p>
  <p class="abs tiny" style="left:13px;top:84px;width:62px;color:#1a1a1a">Lorem ipsum dolor sit amet, consectetuer adipiscing elit, sed diam nonummy nibh euismod tincidunt ut laoreet dolore magna.</p>
  <svg class="abs" style="left:95px;top:14px" width="140" height="62" viewBox="0 0 140 62">
    <defs><linearGradient id="hub" x1="0" y1="0" x2="0" y2="1"><stop offset="0" stop-color="#2ee6dc"/><stop offset="1" stop-color="#2bbaf5"/></linearGradient></defs>
    <circle cx="70" cy="42" r="11" fill="none" stroke="url(#hub)" stroke-width="5"/>
    <circle cx="43" cy="35" r="8" fill="url(#hub)"/><circle cx="60" cy="19" r="8" fill="url(#hub)"/><circle cx="80" cy="19" r="8" fill="url(#hub)"/><circle cx="97" cy="35" r="8" fill="url(#hub)"/>
    <g font-family="Open Sans" font-size="2.2" text-anchor="middle" fill="#222"><text x="43" y="38">Option A</text><text x="60" y="22">Option B</text><text x="80" y="22">Option C</text><text x="97" y="38">Option D</text></g>
    <g font-family="Open Sans" font-size="2.6" font-weight="700" fill="#222"><text x="18" y="24">Your Title</text><text x="40" y="6">Your Title</text><text x="88" y="6">Your Title</text><text x="108" y="22">Your Title</text></g>
  </svg>
  <div class="abs" style="left:98px;top:88px;width:9px;height:9px;border-radius:50%;background:var(--grad)"></div>
  <div class="abs" style="left:98px;top:104px;width:9px;height:9px;border-radius:50%;background:var(--grad)"></div>
  <div class="abs" style="left:165px;top:88px;width:9px;height:9px;border-radius:50%;background:var(--grad)"></div>
  <div class="abs" style="left:165px;top:104px;width:9px;height:9px;border-radius:50%;background:var(--grad)"></div>
  <p class="abs tiny" style="left:110px;top:88px;width:50px"><b style="color:var(--sky)">TITLE</b><br>Lorem ipsum dolor sit amet, consectetuer elit</p>
  <p class="abs tiny" style="left:110px;top:104px;width:50px"><b style="color:var(--sky)">TITLE</b><br>Lorem ipsum dolor sit amet, consectetuer elit</p>
  <p class="abs tiny" style="left:177px;top:88px;width:50px"><b style="color:var(--sky)">TITLE</b><br>Lorem ipsum dolor sit amet, consectetuer elit</p>
  <p class="abs tiny" style="left:177px;top:104px;width:50px"><b style="color:var(--sky)">TITLE</b><br>Lorem ipsum dolor sit amet, consectetuer elit</p>
  <div class="mini-brand">Trevolina</div>
  <div class="page-no">09</div>
</section>

<!-- 10 Roadmap -->
<section class="slide small" style="left:584px;top:838px">
  <div class="abs" style="left:0;top:30px;width:80px;height:77px;background:linear-gradient(90deg,var(--lilac),var(--sky) 50%,var(--cyan))"></div>
  <h2 class="abs" style="left:17px;top:34px;font:400 6px/8px Open Sans,sans-serif;letter-spacing:1px;color:#222">TIMELINE OF<br><span style="font-size:10px;letter-spacing:.5px">ROADMAP</span></h2>
  <p class="abs" style="left:17px;top:56px;font:400 4px Open Sans,sans-serif">FOR 2 YEARS</p>
  <div class="abs" style="left:19px;top:67px;width:11px;height:11px;border-radius:50%;background:#fff;font:700 6px/11px Poppins,sans-serif;text-align:center">A</div>
  <div class="abs" style="left:19px;top:89px;width:11px;height:11px;border-radius:50%;background:#fff;font:700 6px/11px Poppins,sans-serif;text-align:center">B</div>
  <p class="abs tiny" style="left:34px;top:66px;width:40px;color:#1a1a1a"><b style="font-size:5px;color:#fff">2019</b><br>Lorem ipsum dolor sit amet</p>
  <p class="abs tiny" style="left:34px;top:88px;width:40px;color:#1a1a1a"><b style="font-size:5px;color:#fff">2020</b><br>Lorem ipsum dolor sit amet</p>
  <p class="abs" style="left:87px;top:82px;font:700 5px Poppins,sans-serif;color:var(--sky)">+3467</p>
  <p class="abs" style="left:87px;top:90px;font:italic 3px/4px Open Sans,sans-serif;color:var(--sky)">Lorem ipsum<br>dolor sit amet elit.</p>
  <div class="photo" role="img" aria-label="Winding road illustration with numbered milestone markers" style="left:90px;top:22px;width:120px;height:70px;background:linear-gradient(160deg,#3a3550,#6d58b0 50%,#2bbaf5)"></div>
  <p class="abs tiny" style="left:210px;top:30px;width:30px"><b style="color:var(--sky)">OPTION</b><br>Lorem ipsum dolor</p>
  <p class="abs tiny" style="left:210px;top:47px;width:30px"><b style="color:var(--sky)">OPTION</b><br>Lorem ipsum dolor</p>
  <p class="abs tiny" style="left:210px;top:64px;width:30px"><b style="color:var(--sky)">OPTION</b><br>Lorem ipsum dolor</p>
  <div class="mini-brand">Trevolina</div>
  <div class="page-no">10</div>
</section>

<!-- 11 Financial funding -->
<section class="slide small" style="left:60px;top:991px">
  <h2 class="abs cyan-title" style="left:14px;top:14px;font-size:9.5px;line-height:11px;letter-spacing:1px">FINANCIAL<br>FUNDING</h2>
  <p class="abs tiny" style="left:14px;top:38px;width:105px">Lorem ipsum dolor sit amet, consectetuer adipiscing elit, sed diam nonummy nibh euismod tincidunt ut laoreet dolore magna aliquam erat volutpat.</p>
  <p class="abs tiny" style="left:14px;top:54px;width:105px">Lorem ipsum dolor sit amet, consectetuer adipiscing elit, sed diam nonummy nibh euismod tincidunt ut laoreet dolore magna aliquam erat volutpat.</p>
  <div class="abs" style="left:0;top:74px;width:128px;height:38px;background:linear-gradient(90deg,var(--sky),var(--cyan))"></div>
  <p class="abs tiny" style="left:22px;top:78px;width:45px;color:#1a1a1a"><b>TITLE</b><br>It is a process to allow an organization to focus resources.</p>
  <p class="abs tiny" style="left:80px;top:78px;width:45px;color:#1a1a1a"><b>TITLE</b><br>Research your target group and narrow your market.</p>
  <p class="abs tiny" style="left:22px;top:96px;width:45px;color:#1a1a1a"><b>TITLE</b><br>Your brand identity is a way to tell your story.</p>
  <p class="abs tiny" style="left:80px;top:96px;width:45px;color:#1a1a1a"><b>TITLE</b><br>Your brand identity is a way to tell your story.</p>
  <svg class="abs" style="left:150px;top:12px" width="80" height="50" viewBox="0 0 80 50" fill="none">
    <g stroke="#d6e6f0" stroke-width=".3"><path d="M4 2v44M14 2v44M24 2v44M34 2v44M44 2v44M54 2v44M64 2v44M74 2v44M4 8h70M4 18h70M4 28h70M4 38h70"/></g>
    <rect x="21" y="2" width="18" height="5" fill="#2ee6dc"/>
    <path d="M4 44C14 26,20 18,34 16S54 24,74 10" stroke="#2bbaf5" stroke-width=".6"/>
    <path d="M4 44C12 30,22 26,34 26S56 16,74 20" stroke="#2ee6dc" stroke-width=".6"/>
    <path d="M4 44C14 36,24 32,34 34S54 30,74 28" stroke="#8fd9f0" stroke-width=".6"/>
  </svg>
  <svg class="abs" style="left:150px;top:78px" width="80" height="48" viewBox="0 0 80 48">
    <ellipse cx="40" cy="26" rx="36" ry="18" fill="#1e9bc7"/>
    <path d="M40 22 L40 4 A36 18 0 0 1 76 22 Z" fill="#2bbaf5"/>
    <path d="M40 22 L76 22 A36 18 0 0 1 44 40 Z" fill="#2ee6dc"/>
    <path d="M40 22 L44 40 A36 18 0 0 1 4 22 Z" fill="#c6b2f3"/>
    <path d="M40 22 L4 22 A36 18 0 0 1 40 4 Z" fill="#5ff0d8"/>
    <ellipse cx="40" cy="22" rx="13" ry="6.5" fill="#fff"/>
    <g font-family="Poppins" font-weight="700" font-size="5" fill="#fff"><text x="47" y="12">20%</text><text x="60" y="27">20%</text><text x="38" y="37">20%</text><text x="11" y="24">40%</text></g>
  </svg>
  <div class="mini-brand">Trevolina</div>
  <div class="page-no">11</div>
</section>

<!-- 12 Quote -->
<section class="slide small dark" style="left:322px;top:991px">
  <div class="photo" role="img" aria-label="Dark blue-teal scene of a hand using a digital interface" style="left:0;top:0;width:247px;height:139px;background:radial-gradient(circle at 30% 40%,#3d5e66,#1f2d38 60%,#172029)"></div>
  <p class="abs" style="left:78px;top:32px;font:italic 700 11px Poppins,sans-serif">//</p>
  <p class="abs" style="left:77px;top:48px;font:300 12px/12px Open Sans,sans-serif;color:#e9e9e9">Lorem ipsum<br>dolor sit amet,</p>
  <p class="abs" style="left:77px;top:73px;font:italic 800 12px/12px Poppins,sans-serif;color:var(--cyan)">consectetuer<br>adipiscing <span style="color:#fff">//</span></p>
  <div class="mini-brand" style="background:transparent;color:#fff">Trevolina</div>
  <div class="page-no">12</div>
</section>

<!-- 13 Thanks -->
<section class="slide small" style="left:584px;top:991px">
  <div class="photo" role="img" aria-label="Hand holding a glowing globe on a dark background" style="left:118px;top:0;width:129px;height:139px;background:radial-gradient(circle at 62% 45%,#b5b5b5,#505050 30%,#262626 60%)"></div>
  <div class="abs" style="left:70px;top:37px;width:74px;height:45px;background:#fff"></div>
  <div class="abs" style="left:15px;top:45px;width:48px;height:48px;border:2px solid var(--sky);border-top-color:var(--cyan);border-left-color:var(--lilac);display:flex;align-items:center;justify-content:center"><span style="font:700 7.5px Poppins,sans-serif">Trevolina</span></div>
  <h2 class="abs" style="left:74px;top:40px;font:800 15px Poppins,sans-serif;color:var(--cyan)">Thanks</h2>
  <p class="abs tiny" style="left:74px;top:60px;width:65px">Lorem ipsum dolor sit amet, consectetuer adipiscing elit, sed.</p>
  <p class="abs tiny" style="left:74px;top:71px;width:65px;color:#1a1a1a"><b>+00 555 0142<br>hello@trevolina.edu<br>trevolina.edu</b></p>
  <span class="abs" style="left:18px;top:120px;width:8px;height:8px;border-radius:50%;background:var(--ink)"></span>
  <span class="abs" style="left:31px;top:120px;width:8px;height:8px;border-radius:50%;background:var(--ink)"></span>
  <span class="abs" style="left:44px;top:120px;width:8px;height:8px;border-radius:50%;background:var(--ink)"></span>
</section>

</body>
</html>
```